Rack Card for IV Infusion Vitamin Supplement bar

We need a very eye catching rack card so that customers would instantly know it is for IV vitamin infusions. We have our previous rack card (pdf) as an example that did not bring in any clients as an example as well as another one that we did not like too much. The bar is for people to feel better with hydration and vitamins.

Target Market(s)

Anyone

Industry/Entity Type

Healthcare

Requirements
Must have
• Logo on rack card
Should not have
• Not pink other than the logo

```html
<!DOCTYPE html>
<html lang="en">
<head>
<meta charset="utf-8">
<title>Maren Health &amp; Wellness – Vitamin Infusions Rack Card</title>
<link rel="stylesheet" href="https://fonts.googleapis.com/css2?family=Poppins:wght@300;400;500;600;700&family=Kaushan+Script&display=swap">
<style>
:root{
  --green:#0d5443;
  --green-deep:#073f32;
  --cream:#edebe1;
  --ink:#1b1b1b;
  --pink:#de3f86;
  --stage:#646464;
  --white:#ffffff;
}
*{box-sizing:border-box;margin:0;padding:0}
html,body{width:1089px;height:1200px;overflow:hidden}
body{background:var(--stage);font-family:"Poppins",sans-serif;position:relative}
.card{position:absolute;top:107px;width:438px;height:985px;background:var(--cream);overflow:hidden;box-shadow:0 6px 18px rgba(0,0,0,.35)}
.card--front{left:92px}
.card--back{left:563px}

/* front */
.hero-photo{position:absolute;left:0;top:0;width:438px;height:440px;
  background:radial-gradient(ellipse at 55% 40%,#2f7a67 0%,#0e5a48 45%,#06392d 100%)}
.water-line{position:absolute;left:0;top:420px;width:438px;height:30px}
.iv-bag{position:absolute;left:30px;top:335px;width:150px;height:230px;border-radius:20px 20px 26px 26px;
  transform:rotate(-14deg);background:linear-gradient(160deg,#e6e9ec 0%,#a9b3bd 40%,#7b6a8a 70%,#d7dde2 100%);opacity:.95}
.brand{position:absolute;left:225px;top:533px;width:175px;text-align:center;color:var(--green);font-weight:600}
.brand__name{display:block;font-size:34px;letter-spacing:9px;line-height:34px;padding-left:9px}
.brand__tag{display:block;font-size:8.5px;letter-spacing:3.4px;line-height:10px;margin-top:3px;padding-left:3px}
.brand__dot{position:absolute;left:65px;top:-64px;width:44px;height:44px;border-radius:50%;background:var(--pink)}
.headline-frame{position:absolute;left:45px;top:636px;width:349px;height:112px;border:1px solid var(--green);border-radius:10px}
.headline{position:absolute;left:0;top:606px;width:438px;text-align:center;color:var(--green);font-weight:600;letter-spacing:-1px}
.headline__line{display:block;font-size:57px;line-height:57px}
.headline__line--first{background:var(--cream);width:236px;margin:0 auto}
.ribbon{position:absolute;left:73px;top:730px;width:296px;height:38px;background:var(--green);color:var(--white);
  clip-path:polygon(0 0,100% 0,94% 50%,100% 100%,0 100%,6% 50%);
  font-weight:300;font-size:29px;line-height:38px;text-align:center}
.cta{position:absolute;left:0;top:790px;width:438px;text-align:center;font-family:"Kaushan Script",cursive;font-size:58px;line-height:80px;color:var(--ink)}
.footer-band{position:absolute;left:0;bottom:0;width:438px;height:80px}
.call-pill{position:absolute;left:50px;top:887px;width:339px;height:38px;background:var(--white);border:2px solid var(--ink);
  border-radius:19px;display:flex;align-items:center;gap:8px}
.call-pill__icon{width:38px;height:38px;margin-left:-2px}
.call-pill__text{font-size:29px;font-weight:600;color:var(--ink);letter-spacing:-.3px}
.website{position:absolute;left:0;top:938px;width:438px;text-align:center;color:var(--white);font-size:26px;font-weight:400}
.website b{font-weight:600}

/* back */
.splash-top{position:absolute;right:0;top:0;width:110px;height:120px;
  background:radial-gradient(circle at 80% 20%,rgba(255,255,255,.7),rgba(237,235,225,0) 70%)}
.section-tab{position:absolute;left:24px;height:28px;display:flex;align-items:center}
.section-tab__label{background:var(--green);color:var(--white);font-weight:700;font-size:15px;height:28px;line-height:28px;
  padding:0 26px 0 10px;clip-path:polygon(0 0,88% 0,100% 100%,0 100%)}
.section-tab__rule{width:200px;height:1px;background:var(--green);align-self:flex-end}
.section-tab--premium{top:27px}
.section-tab--addons{top:589px}
.menu{position:absolute;left:24px;width:395px;list-style:none}
.menu--premium{top:68px}
.menu--addons{top:639px}
.menu__item{position:relative;padding-left:22px;margin-bottom:7.5px}
.menu__item::before{content:"";position:absolute;left:1px;top:4px;width:8px;height:8px;border-radius:50%;background:var(--pink)}
.menu__item--spaced{margin-bottom:21px}
.menu__item--nodot::before{display:none}
.menu__title{display:block;color:var(--green);font-weight:700;font-size:14px;line-height:15px}
.menu__desc{display:block;color:var(--ink);font-size:11.6px;line-height:14px}
.fruit-photo{position:absolute;left:215px;top:685px;width:223px;height:215px;
  background:radial-gradient(ellipse at 65% 60%,rgba(242,163,38,.85) 0%,rgba(216,53,60,.7) 35%,rgba(155,176,74,.45) 60%,rgba(237,235,225,0) 78%)}
.back-footer{position:absolute;left:0;bottom:0;width:438px;height:100px}
.back-footer__text{position:absolute;left:0;top:913px;width:438px;text-align:center;color:var(--white);font-size:17px;line-height:20px;font-weight:300}
.back-footer__address{position:absolute;left:0;top:960px;width:438px;display:flex;justify-content:center;align-items:center;gap:8px;color:var(--white);font-size:13px}
</style>
</head>
<body>

<section class="card card--front" aria-label="Front of rack card">
  <div class="hero-photo" role="img" aria-label="Smiling woman holding a halved orange over one eye against a deep green water-splash background"></div>
  <svg class="water-line" viewBox="0 0 438 30" preserveAspectRatio="none" aria-hidden="true">
    <path d="M0 0 H438 V18 C360 26 300 10 220 20 C140 28 70 12 0 22 Z" fill="#0e5a48"/>
  </svg>
  <div class="iv-bag" role="img" aria-label="Clear IV bag filled with fresh fruit pieces"></div>

  <div class="brand">
    <span class="brand__dot" aria-hidden="true"></span>
    <span class="brand__name">MAREN</span>
    <span class="brand__tag">HEALTH &amp; WELLNESS</span>
  </div>

  <div class="headline-frame" aria-hidden="true"></div>
  <h1 class="headline">
    <span class="headline__line headline__line--first">VITAMIN</span>
    <span class="headline__line">INFUSIONS</span>
  </h1>
  <div class="ribbon">AND INJECTIONS</div>

  <p class="cta">Book Now!</p>

  <svg class="footer-band" viewBox="0 0 438 80" preserveAspectRatio="none" aria-hidden="true">
    <path d="M0 20 C120 -4 320 -4 438 20 V80 H0 Z" fill="#0d5443"/>
  </svg>
  <div class="call-pill">
    <svg class="call-pill__icon" viewBox="0 0 38 38" aria-hidden="true">
      <circle cx="19" cy="19" r="18" fill="#111"/>
      <path d="M13 11c1-1 2-1 3 0l2 3c.6 1 .4 2-.4 2.6l-1.2 1c.8 2 2.4 3.6 4.4 4.4l1-1.2c.6-.8 1.6-1 2.6-.4l3 2c1 1 1 2 0 3l-1.4 1.4c-1.6 1.6-5 .6-8.6-3S9.4 15.2 11 13.6Z" fill="#fff"/>
    </svg>
    <span class="call-pill__text">Call 555-013-0247</span>
  </div>
  <p class="website">www.<b>marenwellhealth</b>.com</p>
</section>

<section class="card card--back" aria-label="Back of rack card">
  <div class="splash-top" role="img" aria-label="Clear water splash"></div>

  <div class="section-tab section-tab--premium">
    <h2 class="section-tab__label">PREMIUM INFUSIONS</h2>
    <span class="section-tab__rule"></span>
  </div>
  <ul class="menu menu--premium">
    <li class="menu__item"><span class="menu__title">MAREN COCKTAIL</span><span class="menu__desc">Reduce stress, fatigue, and boost your energy. Maren client favorite! (IV fluids, Vitamin C, B-complex, B12, and electrolytes)</span></li>
    <li class="menu__item"><span class="menu__title">IMMUNE SUPPORT</span><span class="menu__desc">Protect the immune system when risk of illness is high. Great for pre, post-travel (IV fluids, Vitamin C, B-complex, and Zinc)</span></li>
    <li class="menu__item"><span class="menu__title">THE GLOW</span><span class="menu__desc">Give a glowing boost to skin and hair from inside out.<br>(IV fluids, Glutathione, Vitamin B-complex, and Biotin)</span></li>
    <li class="menu__item"><span class="menu__title">SPORTS RECOVERY</span><span class="menu__desc">Recover fast from illness, exhaustion, and workouts.<br>(IV fluids, B-complex, B12, and amino acids, and electrolytes)</span></li>
    <li class="menu__item"><span class="menu__title">ENERGIZED</span><span class="menu__desc">Boost metabolism, burn fat easier, and feel energized. (IV fluids, B-complex, and amino acid blend)</span></li>
    <li class="menu__item"><span class="menu__title">BRAIN POWER</span><span class="menu__desc">Support overall brain function, increase memory recall and improve certain aspects of learning. (IV fluids, B6, alpha lipoic acid, and taurine)</span></li>
    <li class="menu__item"><span class="menu__title">THE JETLAG DRIP</span></li>
    <li class="menu__item"><span class="menu__title">THE MIGRAINE / PMS DRIP</span></li>
    <li class="menu__item"><span class="menu__title">THE HANGOVER DRIP</span></li>
    <li class="menu__item menu__item--spaced"><span class="menu__title">NAD+ 125G/ 250G/ 500G DRIP</span><span class="menu__desc">Enhance your cognitive health and help reverse aging. Promotes cell regeneration. Can aid mental clarity, better sleep, and energy.</span></li>
    <li class="menu__item"><span class="menu__title">HIGH DOSE VITAMIN C</span><span class="menu__desc">*Medical clearance required</span></li>
  </ul>

  <div class="section-tab section-tab--addons">
    <h2 class="section-tab__label">INFUSIONS ADD-ONS</h2>
    <span class="section-tab__rule"></span>
  </div>
  <div class="fruit-photo" role="img" aria-label="Oranges, kiwi, strawberries and berries splashing into water"></div>
  <ul class="menu menu--addons">
    <li class="menu__item"><span class="menu__title">GLUTATHIONE</span><span class="menu__desc">*A powerful natural antioxidant to help Detox</span></li>
    <li class="menu__item"><span class="menu__title">ADDITIONAL VITAMIN C</span></li>
    <li class="menu__item"><span class="menu__title">ADDITIONAL ZINC</span></li>
    <li class="menu__item"><span class="menu__title">ADDITIONAL MAGNESIUM</span></li>
    <li class="menu__item"><span class="menu__title">ANTI- INFLAMMATION<br>MEDICATION</span></li>
    <li class="menu__item"><span class="menu__title">ANTI-NAUSEA MEDICATION</span></li>
    <li class="menu__item"><span class="menu__title">VITAMIN D SHOT</span></li>
    <li class="menu__item menu__item--nodot"><span class="menu__title">VITAMIN B12 SHOT</span></li>
  </ul>

  <svg class="back-footer" viewBox="0 0 438 100" preserveAspectRatio="none" aria-hidden="true">
    <path d="M0 30 C110 -2 320 -4 438 30 V100 H0 Z" fill="#0d5443"/>
  </svg>
  <p class="back-footer__text">By appointments only,<br>including weekends 555-013-0247</p>
  <p class="back-footer__address">
    <svg width="15" height="15" viewBox="0 0 16 16" aria-hidden="true">
      <circle cx="8" cy="8" r="7.5" fill="#fff"/>
      <path d="M8 3.5a3 3 0 0 0-3 3c0 2.2 3 5.5 3 5.5s3-3.3 3-5.5a3 3 0 0 0-3-3Z" fill="#111"/>
      <circle cx="8" cy="6.5" r="1.1" fill="#fff"/>
    </svg>
    1420 Elm Grove Ave., Suite 2B Riverton
  </p>
</section>

</body>
</html>
```